Car rental website design for a UAE car rental company

This project is about creating a new website design for a car rental company located in Dubai (United Arab Emirates), I opened the same project a few months ago but I didn't receive a lot of appealing entries so I closed it but this time I am marking the project as guaranteed to avoid such situation again, if you have already provided a design before then please re-submit again on this project so that it is considered while reviewing all the designs

A few important things:

1- We need a simple non-complex design
2- The final deliverable would be 2 screens (PSD, JPEG ... etc), the first screen is for the home page and the second screen is for an internal page
3- The home page must have a section that end users can use to rent a car online directly from the home page instead of going into some inner pages
4- The current website is very old and not very appealing so avoid creating a similar design (www.quarvin-drive.example)
5- The name is Quarvin but the company rents normal cars (no Limousin cars will be rented) so avoid adding any fancy cars in the images/graphics used in the design, just normal end users cars
6- The expected pages would be: home, About us, Our team, Strategy, Contact us and links to social media pages
7- The attachments include the company's logo and some screens from other car rental companies that provide online rentals/payments

If you have any questions please feel free to ask and please note that we will need the designs urgently

Thanks

Target Market(s)

Dubai - United Arab Emirates

Industry/Entity Type

It Company

Number of Pages Required

2 page

Font styles to use
Sans Serif

Requirements
Must have
• Check the project details
Nice to have
Should not have

```html
<!DOCTYPE html>
<html lang="en">
<head>
<meta charset="utf-8">
<title>Quarvin Rent A Car</title>
<link rel="stylesheet" href="https://fonts.googleapis.com/css2?family=Source+Sans+3:wght@400;600;700&family=Raleway:wght@600;700&family=Arimo:wght@400;700&display=swap">
<style>
:root{
  --brand:#a50d35;
  --ink:#333;
  --muted:#777;
  --line:#d8d8d8;
  --page:#efefef;
  --white:#fff;
  --black:#000;
}
*{box-sizing:border-box;margin:0;padding:0}
html,body{width:1001px;height:1200px;overflow:hidden;background:var(--page)}
body{font-family:"Arimo",Arial,sans-serif;color:var(--ink)}
.page{position:absolute;left:0;top:0;width:1200px;height:1439px;transform:scale(.83417);transform-origin:0 0;background:var(--page)}
.abs{position:absolute}
.header{left:0;top:0;width:1200px;height:153px;background:var(--white)}
.brand-mark{left:148px;top:10px;width:64px;height:72px;border:3px solid var(--brand)}
.brand-name{left:100px;top:84px;font-family:"Source Sans 3",sans-serif;font-weight:600;font-size:36px;color:#8a938c}
.call{display:flex;align-items:flex-start;gap:8px}
.call-title{font-family:"Raleway",sans-serif;font-weight:700;font-size:30px;line-height:30px}
.call-num{font-size:18px;letter-spacing:.5px;margin-top:8px}
.call-top{left:905px;top:16px;color:var(--brand)}
.call-top .call-num{color:var(--ink)}
.nav{left:457px;top:107px;display:flex;align-items:center;font-size:15px;color:#444}
.nav a{color:inherit;text-decoration:none;margin-right:79px}
.nav a.active{background:var(--brand);color:var(--white);width:76px;height:36px;display:flex;align-items:center;justify-content:center;margin-right:60px}
.hero{left:0;top:153px;width:1200px;height:357px;background:linear-gradient(180deg,#4f79b0 0%,#7fa0c8 45%,#5f7d8f 100%)}
.booking{left:100px;top:236px;width:460px;height:379px;background:var(--white);border-radius:4px;box-shadow:0 1px 3px rgba(0,0,0,.12);border-top:3px solid var(--brand)}
.tab{top:0;height:45px;display:flex;align-items:center;justify-content:center;font-family:"Source Sans 3",sans-serif;font-size:17px;letter-spacing:1px}
.tab-book{left:0;width:234px;color:#444;font-weight:600}
.tab-manage{left:234px;width:226px;background:var(--brand);color:var(--white);font-weight:700}
.field{border:1px solid var(--line);border-radius:5px;background:var(--white)}
.label{font-size:14px;color:#555}
.placeholder{font-size:14px;color:#999}
.continue{left:327px;top:302px;width:110px;height:49px;background:var(--brand);color:var(--white);border-radius:5px;font-size:18px;display:flex;align-items:center;justify-content:center}
.hero-copy{right:103px;top:250px;text-align:right;color:var(--white);font-family:"Source Sans 3",sans-serif}
.hero-title{font-size:35px;font-weight:700;letter-spacing:2px;text-shadow:0 1px 2px rgba(0,0,0,.3)}
.hero-sub{font-size:25px;margin-top:10px}
.hero-more{font-size:15px;margin-top:14px;display:flex;justify-content:flex-end;align-items:center;gap:7px}
.hero-cars{left:600px;top:400px;width:500px;height:198px;border-radius:40px 60px 10px 10px;background:linear-gradient(100deg,#2a2a2a 0%,#444 40%,#c22a45 60%,#d63a55 100%)}
.section-title{left:0;top:692px;width:1200px;text-align:center;font-family:"Source Sans 3",sans-serif;font-weight:700;font-size:34px;color:var(--brand)}
.rule{height:1px;background:#bbb;top:714px}
.card{background:var(--white);border:1px solid var(--line);border-radius:6px}
.card.featured{border-color:var(--brand);box-shadow:0 0 5px rgba(0,0,0,.15)}
.card-title{position:absolute;left:0;width:100%;text-align:center;font-family:"Source Sans 3",sans-serif;font-size:24px;color:var(--ink);letter-spacing:.5px}
.car-pic{position:absolute;border-radius:40px 50px 14px 14px;background:linear-gradient(180deg,#d8d8d8,#9a9a9a)}
.model{position:absolute;left:0;width:100%;text-align:center;font-family:"Source Sans 3",sans-serif;font-size:18px;color:var(--muted)}
.featured .model{color:var(--ink);font-weight:600}
.specs{position:absolute;list-style:none;font-size:13px;color:#333}
.specs li{height:26px;display:flex;align-items:center;gap:9px}
.specs svg{width:15px;height:15px}
.card-foot{position:absolute;left:11px;right:11px;border-top:1px solid var(--line)}
.price{position:absolute;font-family:"Source Sans 3",sans-serif;font-size:17px;color:var(--brand)}
.select{position:absolute;width:72px;height:32px;background:var(--brand);color:var(--white);border-radius:5px;font-family:"Source Sans 3",sans-serif;font-size:16px;display:flex;align-items:center;justify-content:center}
.footer{left:0;top:1260px;width:1200px;height:142px;background:var(--black);color:var(--white)}
.share{left:122px;top:22px;font-family:"Source Sans 3",sans-serif;font-size:18px}
.social{left:122px;top:64px;display:flex;gap:12px}
.social span{width:33px;height:33px;border-radius:50%;background:#8a8a8a}
.foot-nav{left:394px;top:61px;font-size:14px;color:#ddd;display:flex;gap:15px}
.call-foot{left:885px;top:32px;color:var(--white)}
.copyright{left:0;top:1402px;width:1200px;height:37px;background:var(--brand);color:var(--white);font-family:"Source Sans 3",sans-serif;font-size:14px;font-weight:600;display:flex;align-items:center;justify-content:center}
</style>
</head>
<body>
<div class="page">
  <header class="header abs">
    <div class="brand-mark abs"></div>
    <div class="brand-name abs">Quarvin</div>
    <div class="call call-top abs">
      <svg width="46" height="64" viewBox="0 0 46 64"><path d="M8 4 L18 2 L22 18 L15 22 Q20 38 32 46 L38 40 L46 50 L40 60 Q18 56 6 28 Z" fill="#a50d35"/></svg>
      <div><div class="call-title">CALL US</div><div class="call-num">+971 4000 7318</div></div>
    </div>
    <nav class="nav abs">
      <a class="active" href="#">Home</a><a href="#">About Us</a><a href="#">Our Team</a><a href="#">Strategy</a><a href="#" style="margin-right:0">Contact Us</a>
    </nav>
  </header>

  <div class="hero abs" role="img" aria-label="Sky with clouds above mountain slopes"></div>
  <div class="hero-copy abs">
    <div class="hero-title">EXPERIENCE AN EXTRA MILE</div>
    <div class="hero-sub">of comfort, pleasure and leisure from the best</div>
    <div class="hero-more"><svg width="13" height="13" viewBox="0 0 14 14"><circle cx="7" cy="7" r="6" fill="none" stroke="#fff" stroke-width="1.3"/><path d="M4 7h6M7.5 4.5 10 7l-2.5 2.5" fill="none" stroke="#fff" stroke-width="1.3"/></svg>Learn More</div>
  </div>
  <div class="hero-cars abs" role="img" aria-label="A black hatchback and a red sedan parked side by side"></div>

  <form class="booking abs">
    <div class="tab tab-book abs">BOOK A CAR</div>
    <div class="tab tab-manage abs">MANAGE RESERVATION</div>
    <div class="field abs" style="left:20px;top:75px;width:423px;height:45px;padding:12px 8px"><span class="placeholder">Enter airport, city or zip code</span></div>
    <div class="field abs" style="left:20px;top:133px;width:25px;height:25px"></div>
    <div class="label abs" style="left:54px;top:139px">Return at diffrent Location</div>
    <div class="label abs" style="left:29px;top:187px">Pick-up date</div>
    <div class="label abs" style="left:251px;top:187px">Drop-off date</div>
    <div class="field abs" style="left:20px;top:212px;width:143px;height:45px"><svg class="abs" style="left:9px;top:15px" width="15" height="15" viewBox="0 0 15 15"><rect x="1" y="2" width="13" height="12" fill="none" stroke="#3a8ee6" stroke-width="1.4"/><path d="M1 5h13M4 8h2M8 8h2M4 11h2M8 11h2" stroke="#3a8ee6"/></svg></div>
    <div class="field abs" style="left:172px;top:212px;width:53px;height:45px"></div>
    <div class="field abs" style="left:237px;top:212px;width:143px;height:45px"><svg class="abs" style="left:11px;top:15px" width="15" height="15" viewBox="0 0 15 15"><rect x="1" y="2" width="13" height="12" fill="none" stroke="#3a8ee6" stroke-width="1.4"/><path d="M1 5h13M4 8h2M8 8h2M4 11h2M8 11h2" stroke="#3a8ee6"/></svg></div>
    <div class="field abs" style="left:390px;top:212px;width:53px;height:45px"></div>
    <div class="label abs" style="left:29px;top:281px">Car Type</div>
    <div class="field abs" style="left:20px;top:306px;width:143px;height:45px;padding:14px 11px"><span class="placeholder">Standard</span><svg class="abs" style="left:119px;top:20px" width="9" height="5"><path d="M0 0h9L4.5 5z" fill="#999"/></svg></div>
    <div class="continue abs">Continue</div>
  </form>

  <div class="rule abs" style="left:130px;width:358px"></div>
  <div class="rule abs" style="left:717px;width:358px"></div>
  <h2 class="section-title abs">Our Vehicles</h2>

  <svg class="abs" style="left:100px;top:918px" width="40" height="125" viewBox="0 0 40 125"><path d="M36 2 L6 62 L36 123" fill="none" stroke="#c8c8c8" stroke-width="6"/></svg>
  <svg class="abs" style="left:1053px;top:914px" width="40" height="125" viewBox="0 0 40 125"><path d="M4 2 L34 62 L4 123" fill="none" stroke="#c8c8c8" stroke-width="6"/></svg>

  <div class="card abs" style="left:186px;top:782px;width:244px;height:401px">
    <div class="card-title" style="top:16px">Small Car</div>
    <div class="car-pic" role="img" aria-label="Small silver hatchback" style="left:40px;top:55px;width:178px;height:105px"></div>
    <div class="model" style="top:182px">Velta Pico or Smilar</div>
    <ul class="specs" style="left:35px;top:210px">
      <li><svg viewBox="0 0 15 15"><circle cx="6" cy="5" r="3" fill="none" stroke="#aaa"/><path d="M1 14q5-8 10 0" fill="none" stroke="#aaa"/></svg>5 passengers</li>
      <li><svg viewBox="0 0 15 15"><rect x="1" y="4" width="13" height="9" fill="#bbb"/></svg>1 large suitcases,1 small</li>
      <li><svg viewBox="0 0 15 15"><circle cx="7.5" cy="7.5" r="7" fill="#bbb"/></svg>automatic transmission</li>
      <li><svg viewBox="0 0 15 15"><path d="M7.5 1v13M1.5 4.5l12 6M1.5 10.5l12-6" stroke="#bbb" stroke-width="1.4"/></svg>air conditioning</li>
      <li><svg viewBox="0 0 15 15"><rect x="2" y="2" width="8" height="12" fill="#bbb"/></svg>13 km/l</li>
    </ul>
    <div class="card-foot" style="top:353px"></div>
    <div class="price" style="left:15px;top:367px">$299.00</div>
    <div class="select" style="left:158px;top:360px">Select</div>
  </div>

  <div class="card abs" style="left:770px;top:782px;width:239px;height:401px">
    <div class="card-title" style="top:16px">Medium Car</div>
    <div class="car-pic" role="img" aria-label="Silver mid-size sedan" style="left:10px;top:55px;width:200px;height:105px"></div>
    <div class="model" style="top:179px">Velta Sorel or similar</div>
    <ul class="specs" style="left:30px;top:207px">
      <li><svg viewBox="0 0 15 15"><circle cx="6" cy="5" r="3" fill="none" stroke="#aaa"/><path d="M1 14q5-8 10 0" fill="none" stroke="#aaa"/></svg>5 passengers</li>
      <li><svg viewBox="0 0 15 15"><rect x="1" y="4" width="13" height="9" fill="#bbb"/></svg>1 large suitcases,1 small</li>
      <li><svg viewBox="0 0 15 15"><circle cx="7.5" cy="7.5" r="7" fill="#bbb"/></svg>automatic transmission</li>
      <li><svg viewBox="0 0 15 15"><path d="M7.5 1v13M1.5 4.5l12 6M1.5 10.5l12-6" stroke="#bbb" stroke-width="1.4"/></svg>air conditioning</li>
      <li><svg viewBox="0 0 15 15"><rect x="2" y="2" width="8" height="12" fill="#bbb"/></svg>13 km/l</li>
    </ul>
    <div class="card-foot" style="top:353px"></div>
    <div class="price" style="left:15px;top:367px">$299.00</div>
    <div class="select" style="left:157px;top:360px">Select</div>
  </div>

  <div class="card featured abs" style="left:431px;top:757px;width:339px;height:452px">
    <div class="card-title" style="top:15px">Large Car</div>
    <div class="car-pic" role="img" aria-label="Silver SUV" style="left:62px;top:85px;width:212px;height:120px"></div>
    <div class="model" style="top:217px">Velta Sorel or similar</div>
    <ul class="specs" style="left:88px;top:251px">
      <li><svg viewBox="0 0 15 15"><circle cx="6" cy="5" r="3" fill="none" stroke="#aaa"/><path d="M1 14q5-8 10 0" fill="none" stroke="#aaa"/></svg>5 passengers</li>
      <li><svg viewBox="0 0 15 15"><rect x="1" y="4" width="13" height="9" fill="#bbb"/></svg>1 large suitcases,1 small</li>
      <li><svg viewBox="0 0 15 15"><circle cx="7.5" cy="7.5" r="7" fill="#bbb"/></svg>automatic transmission</li>
      <li><svg viewBox="0 0 15 15"><path d="M7.5 1v13M1.5 4.5l12 6M1.5 10.5l12-6" stroke="#bbb" stroke-width="1.4"/></svg>air conditioning</li>
      <li><svg viewBox="0 0 15 15"><rect x="2" y="2" width="8" height="12" fill="#bbb"/></svg>13 km/l</li>
    </ul>
    <div class="card-foot" style="top:397px;left:14px;right:14px"></div>
    <div class="price" style="left:23px;top:415px">$299.00</div>
    <div class="select" style="left:245px;top:408px">Select</div>
  </div>

  <footer class="footer abs">
    <div class="share abs">Share Your Love for us !</div>
    <div class="social abs"><span></span><span></span><span></span></div>
    <div class="foot-nav abs"><span>Home</span><span>|</span><span>About Us</span><span>|</span><span>Our Team</span><span>|</span><span>Strategy</span><span>|</span><span>Contact Us</span></div>
    <div class="call call-foot abs">
      <svg width="46" height="64" viewBox="0 0 46 64"><path d="M8 4 L18 2 L22 18 L15 22 Q20 38 32 46 L38 40 L46 50 L40 60 Q18 56 6 28 Z" fill="#a50d35"/></svg>
      <div><div class="call-title">CALL US</div><div class="call-num">+971 4000 7318</div></div>
    </div>
  </footer>
  <div class="copyright abs">©Copyright 2011, Quarvin. All rights reserved.</div>
</div>
</body>
</html>
```